RJ Penhall & Associates

Create a website encompassing design work already carried out for business card.
Small accounting practice, business accounting and management, superannuation, audit, taxation.

```html
<!DOCTYPE html>
<html lang="en">
<head>
<meta charset="utf-8">
<title>RJ Penhall &amp; Associates</title>
<link rel="stylesheet" href="https://fonts.googleapis.com/css2?family=Open+Sans:ital,wght@0,400;0,600;0,700;1,700&display=swap">
<style>
:root{
  --page-bg:#efefef;
  --panel:#ffffff;
  --ink:#3a3a3a;
  --text:#4a4a4a;
  --muted:#777;
  --brand:#45ade0;
  --button:#0ea3e4;
  --link:#19a3dc;
  --accent:#f26a10;
  --rule:#dcdcdc;
  --nav-top:#a5a5a5;
  --nav-bottom:#5f5f5f;
}
*{box-sizing:border-box;margin:0;padding:0}
html,body{width:1142px;height:1200px;overflow:hidden}
body{background:var(--page-bg);font-family:"Open Sans",Arial,sans-serif;color:var(--text);position:relative}
.site{position:absolute;left:90px;top:0;width:952px;height:1105px;background:var(--panel);box-shadow:0 0 3px rgba(0,0,0,.15)}
.brand{position:absolute;left:24px;top:24px;display:flex;align-items:center;gap:14px}
.brand-mark{width:56px;height:56px;background:var(--brand)}
.brand-name{font-weight:700;font-size:22px;line-height:24px;color:#222;width:160px}
.contact{position:absolute;right:20px;top:30px;text-align:right}
.phone{font-size:14px;color:#222;display:flex;align-items:center;gap:6px;justify-content:flex-end}
.social{display:flex;gap:10px;justify-content:flex-end;margin-top:12px}
.social span{width:22px;height:22px;border-radius:50%;background:var(--brand)}
.tagline{position:absolute;left:0;top:100px;width:952px;height:26px;background:var(--brand);color:#fff;font-size:9.5px;font-weight:600;padding:6px 24px}
.nav{position:absolute;left:0;top:126px;width:952px;height:41px;background:linear-gradient(var(--nav-top),var(--nav-bottom));display:flex;box-shadow:0 4px 6px rgba(0,0,0,.12)}
.nav a{color:#fff;text-decoration:none;font-weight:700;font-size:13px;line-height:41px;padding:0 25px;border-right:1px solid rgba(255,255,255,.35)}
.nav a:first-child{padding:0 22px}
.hero{position:absolute;left:21px;top:187px;width:910px;height:298px;border-radius:5px;background:linear-gradient(100deg,#f4f4f4 0%,#dedede 45%,#9a9a9a 75%,#cfcfcf 100%)}
.hero-text{position:absolute;left:67px;top:124px;color:#555}
.hero-text .l1{font-size:29px;font-weight:600}
.hero-text .l1 small{font-size:20px;font-weight:400}
.hero-text .l2{font-size:11px;margin-top:0}
.hero-text .l2 b{font-size:27px;font-weight:400;color:var(--accent)}
.welcome{position:absolute;left:23px;top:505px;width:900px}
.welcome h1{font-size:26px;font-weight:600;color:var(--ink);margin-bottom:6px}
.welcome p{font-size:13px;line-height:24px}
.welcome a{color:var(--link);text-decoration:none;font-size:13.5px}
.card{position:absolute;top:655px;width:292px;height:302px;border:1px solid var(--rule);border-radius:4px;background:linear-gradient(#fff 60%,#ececec);padding:22px 22px 0}
.card h2{font-size:21px;font-weight:600;color:var(--ink);margin-bottom:16px}
.services li{list-style:none;display:flex;align-items:center;gap:10px;font-size:13.5px;height:38px;border-bottom:1px solid var(--rule)}
.services li:last-child{border-bottom:0}
.services i{width:22px;height:22px;border-radius:50%;border:1px solid #ccc;background:#f6f6f6}
.news{font-size:13.5px;line-height:23px;padding-left:6px}
.news .date{font-size:12px;color:var(--muted)}
.news b{font-weight:700;color:#333}
.quote{font-size:13.5px;line-height:24px;padding-left:4px}
.quote cite{display:block;font-weight:700;font-style:italic;color:#333;margin-top:6px}
.btn{position:absolute;left:24px;bottom:12px;background:var(--button);color:#fff;font-weight:700;font-size:13.5px;padding:6px 14px;border-radius:3px;text-decoration:none}
.partners{position:absolute;left:20px;top:1000px;width:920px;display:flex;justify-content:space-between;align-items:center}
.partners span{font-size:16px;font-weight:400;color:#9b9b9b;width:140px;text-align:center}
.footer{position:absolute;left:0;top:1124px;width:1142px;text-align:center;font-size:13.5px;color:#555}
.footer nav{display:flex;justify-content:center;gap:21px;margin-bottom:6px}
.footer nav a{color:#555;text-decoration:none}
</style>
</head>
<body>
<div class="site">
  <header>
    <div class="brand"><span class="brand-mark"></span><span class="brand-name">RJ Penhall &amp; Associates</span></div>
    <div class="contact">
      <div class="phone"><svg width="8" height="16" viewBox="0 0 8 16"><path d="M6 1C1 4 1 12 6 15" stroke="#45ade0" stroke-width="3" fill="none" stroke-linecap="round"/></svg>+1 (555) 214 7730</div>
      <div class="social"><span></span><span></span><span></span><span></span></div>
    </div>
  </header>
  <div class="tagline">Accountant · Business Solutions · Management · Superannuation · Audit</div>
  <nav class="nav"><a>HOME</a><a>ABOUT US</a><a>SERVICES</a><a>LATEST NEWS</a><a>TESTIMONIALS</a><a>FAQ</a><a>CONTACT US</a></nav>
  <section class="hero" role="img" aria-label="Black and white photo of three business people working at a laptop in a glass office">
    <div class="hero-text">
      <div class="l1">BUSINESS <small>MANAGEMENT</small></div>
      <div class="l2">FOR <b>YOUR BUSINESS</b></div>
    </div>
  </section>
  <section class="welcome">
    <h1>Welcome to</h1>
    <p>Lorem Ipsum is simply dummy text of the printing and typesetting industry. Lorem Ipsum has been the industry's standard dummy text ever since the 1500s, when an unknown printer took a galley of type and scrambled it to make a type specimen book. It has survived not only five centuries, but also the leap into electronic typesetting, remaining essentially unchanged. It was popularised in the 1960s with the release of Letraset .</p>
    <a href="#">Click Here</a>
  </section>
  <section class="card" style="left:25px">
    <h2>OUR SERVICES</h2>
    <ul class="services">
      <li><i></i>Accounting</li><li><i></i>Business Management</li><li><i></i>Audit</li><li><i></i>Superannuation</li><li><i></i>Tax</li>
    </ul>
    <a class="btn" href="#">Know More</a>
  </section>
  <section class="card" style="left:334px">
    <h2>LATEST NEWS</h2>
    <div class="news">
      <div class="date">13/09/2014</div>
      <p><b>Lorem Ipsum is simply dummy</b><br>text of the printing and typesetting industry. Lorem Ipsum .</p>
      <div class="date">13/09/2014</div>
      <p style="margin-top:4px"><b>Lorem Ipsum is simply dummy</b><br>text of the printing and typesetting industry. Lorem Ipsum .</p>
    </div>
    <a class="btn" href="#" style="left:30px">Know More</a>
  </section>
  <section class="card" style="left:643px">
    <h2>TESTIMONIALS</h2>
    <div class="quote">Lorem Ipsum is simply dummy text of the printing and typesetting industry. Lorem Ipsum has been the industry's standard dummy text ever since the 1500s, when an unknown printer took a galley of type and scrambled.<cite>Sam, Leeds</cite></div>
    <a class="btn" href="#" style="left:29px">Know More</a>
  </section>
  <div class="partners">
    <span>Harbour Gate</span><span>BrightLedger</span><span>Northfield</span><span>Whitcombe Vale</span><span>Stoneridge</span><span>The Meridian Group</span>
  </div>
</div>
<footer class="footer">
  <nav><a>Home</a><a>About us</a><a>Services</a><a>Latest News</a><a>Testimonials</a><a>Contact Us</a></nav>
  <p>Copyright © 2014 RJ Penhall &amp; Associates. All rights reserved.</p>
</footer>
</body>
</html>
```